Custom Cabinet Shop Needs a website design

Hi,
We need a website for a Custom Cabinet Shop and Cabinet parts manufacturing business.
The business has two sides to it. One side provides custom Kitchens, vanities, entertainment units, offices and what not to homeowners and contractors.
The 2nd side of the business provides built to order cabinet boxes and other parts required to put together a project to other cabinet shops, small contractors looking to install there own cabinets.
Website will need a Gallery to display work.
Color scheme to go well with logo.
current website is www.brindlewoodcustomcabinets.com
being changed to www.brindlewood.ca
Logo Included in attached files.
Tagline "Millwork with Flare"
Mission Statement "Our passion is to deliver inspired cabinetry solutions to suit all your needs, supported by our phenomenal star class customer service"
The website should convey quality and professionalism.
Thank you.
Homeowners/ Contractors
Entertainment
Coded - Design and coding required
1 page

```html
<!DOCTYPE html>
<html lang="en">
<head>
<meta charset="utf-8">
<title>Brindlewood Custom Cabinets — Millwork with Flare</title>
<link rel="stylesheet" href="https://fonts.googleapis.com/css2?family=Great+Vibes&family=Quicksand:wght@400;500;700&display=swap">
<style>
  :root{
    --orange:#e8794a;
    --orange-soft:rgba(232,121,74,.85);
    --orange-dark:#c4562a;
    --icon-bg:#1a0c06;
    --black:#000;
    --ink:#0b0b0b;
    --white:#fff;
    --grey:#d4d4d4;
  }
  *{margin:0;padding:0;box-sizing:border-box}
  html,body{width:1200px;height:2871px;overflow:hidden;background:var(--black)}
  body{position:relative;font-family:"Quicksand",sans-serif;color:var(--white)}
  .script{font-family:"Great Vibes",cursive;font-weight:400}

  /* Hero */
  .hero{position:absolute;left:0;top:0;width:1200px;height:677px;
    background:
      radial-gradient(ellipse 260px 200px at 560px 330px,rgba(196,140,88,.55),rgba(0,0,0,0) 75%),
      radial-gradient(ellipse 160px 260px at 190px 310px,rgba(70,60,58,.8),rgba(0,0,0,0) 80%),
      linear-gradient(90deg,#1b2330 0%,#22262e 18%,#2c2420 35%,#3a2a20 60%,#4e382c 80%,#6a4e3e 100%);}
  .hero-floor{position:absolute;left:0;bottom:0;width:1200px;height:200px;
    background:linear-gradient(180deg,rgba(90,48,26,0) 0%,rgba(96,52,28,.85) 55%,rgba(70,36,20,1) 100%)}
  .hero-ceiling{position:absolute;left:0;top:0;width:1200px;height:130px;
    background:linear-gradient(180deg,#1a1a1c 0%,rgba(40,32,28,.6) 70%,rgba(0,0,0,0) 100%)}
  .topbar{position:absolute;left:0;top:0;width:1200px;height:62px;display:flex;align-items:center;padding:0 165px}
  .brand{display:flex;align-items:center;gap:9px;font-weight:700;font-size:16px;letter-spacing:2px;color:var(--white)}
  .brand-dot{width:20px;height:20px;border-radius:50%;background:var(--orange)}
  .nav{margin-left:auto;display:flex;gap:52px;font-size:10px;letter-spacing:1.5px;font-weight:500;padding-right:2px}
  .tagline{position:absolute;left:0;width:1200px;text-align:center;font-size:128px;line-height:1;color:var(--white);text-shadow:0 3px 10px rgba(0,0,0,.55)}

  /* Bands */
  .band{position:absolute;left:0;width:1200px;height:55px;background:var(--orange)}
  .band-title{position:absolute;left:158px;top:8px;font-size:30px;color:var(--white)}

  /* About */
  .about{position:absolute;left:0;top:732px;width:1200px;height:640px;
    background:
      radial-gradient(ellipse 300px 140px at 820px 300px,rgba(214,76,62,.35),rgba(0,0,0,0) 80%),
      radial-gradient(ellipse 260px 120px at 420px 300px,rgba(232,196,70,.35),rgba(0,0,0,0) 80%),
      linear-gradient(180deg,#d8d2bd 0%,#b9b79a 22%,#8c8a62 40%,#d9d2c0 52%,#7a5a46 66%,#3a2418 82%,#24160f 100%);}
  .about-side{position:absolute;left:0;top:0;width:1200px;height:640px;
    background:linear-gradient(90deg,rgba(30,24,28,.75) 0%,rgba(30,24,28,.4) 12%,rgba(0,0,0,0) 28%,rgba(0,0,0,0) 88%,rgba(240,236,226,.5) 100%)}
  .mission{position:absolute;left:0;top:318px;width:1200px;text-align:center;font-size:22px;line-height:1.35;font-weight:500;letter-spacing:.4px;text-shadow:0 2px 6px rgba(0,0,0,.7)}

  /* Services */
  .services{position:absolute;left:0;top:1427px;width:1200px;height:542px;background:var(--black)}
  .service-icon{position:absolute;top:123px}
  .service-name{position:absolute;top:320px;width:380px;text-align:center;font-size:32px}
  .service-text{position:absolute;top:366px;width:380px;font-size:11.5px;line-height:2.05;letter-spacing:.6px;color:var(--grey);font-weight:500}

  /* Gallery */
  .gallery{position:absolute;left:0;top:1969px;width:1200px;height:606px;background:var(--black)}
  .shot{position:absolute;top:0;height:606px;overflow:hidden}
  .shot-strip{position:absolute;left:0;top:0;width:100%;height:63px;background:var(--orange-soft)}
  .gallery-title{position:absolute;left:162px;top:10px;font-size:32px}
  .arrow{position:absolute;top:272px;width:46px;height:46px;background:var(--orange-dark);display:flex;align-items:center;justify-content:center}

  /* Footer */
  .footer{position:absolute;left:0;top:2575px;width:1200px;height:296px;background:var(--ink)}
  .footer .brand{position:absolute;left:0;top:68px;width:1200px;justify-content:center;font-size:20px}
  .copyright{position:absolute;left:0;top:144px;width:1200px;text-align:center;font-size:13px;letter-spacing:1.5px;color:var(--grey)}
  .socials{position:absolute;left:0;top:194px;width:1200px;display:flex;justify-content:center;gap:22px}
  .social{width:14px;height:14px;border-radius:50%;border:2px solid var(--white)}
</style>
</head>
<body>

<header class="hero" role="img" aria-label="Photo of a dark custom kitchen with a live-edge island, bar stools and pendant lights">
  <div class="hero-ceiling"></div>
  <div class="hero-floor"></div>
  <div class="topbar">
    <div class="brand"><span class="brand-dot"></span>BRINDLEWOOD</div>
    <nav class="nav"><span>ABOUT</span><span>PORTFOLIO</span><span>JOURNAL</span><span>FEATURES</span><span>CONTACT</span></nav>
  </div>
  <h1 class="tagline script" style="top:222px">"Millwork with</h1>
  <h1 class="tagline script" style="top:380px">Flare"</h1>
</header>

<div class="band" style="top:677px"><h2 class="band-title script">A little About us</h2></div>

<section class="about" role="img" aria-label="Photo of a sunny breakfast nook with a wood table, upholstered chairs and cushioned bench">
  <div class="about-side"></div>
  <p class="mission">“Our passion is to deliver inspired cabinetry solutions<br>to suit all your needs, supported by<br>our phenomenal star class customer service.”</p>
</section>

<div class="band" style="top:1372px"><h2 class="band-title script">Services</h2></div>

<section class="services">
  <svg class="service-icon" style="left:267px" width="184" height="184" viewBox="0 0 190 190">
    <circle cx="95" cy="95" r="92" fill="none" stroke="#e8794a" stroke-width="2"/>
    <circle cx="95" cy="95" r="84" fill="#1a0c06"/>
    <path d="M55 98 L95 60 L135 98 L124 98 L124 132 L103 132 L103 108 L87 108 L87 132 L66 132 L66 98 Z" fill="#e8794a"/>
    <rect x="114" y="64" width="10" height="20" fill="#e8794a"/>
  </svg>
  <h3 class="service-name script" style="left:169px">Residential</h3>
  <p class="service-text" style="left:172px">Kitchens, vanities, entertainment units and home offices built to order for homeowners and contractors, finished with care in our own shop.</p>

  <svg class="service-icon" style="left:680px" width="184" height="184" viewBox="0 0 190 190">
    <circle cx="95" cy="95" r="92" fill="none" stroke="#e8794a" stroke-width="2"/>
    <circle cx="95" cy="95" r="84" fill="#1a0c06"/>
    <path d="M58 60 H132 L138 82 H52 Z" fill="#e8794a"/>
    <path d="M52 84 H138 V92 Q131 100 124 92 Q117 100 110 92 Q103 100 95 92 Q88 100 81 92 Q74 100 66 92 Q59 100 52 92 Z" fill="#e8794a"/>
    <rect x="60" y="102" width="70" height="34" fill="#e8794a"/>
    <rect x="68" y="108" width="22" height="16" fill="#1a0c06"/>
    <rect x="98" y="108" width="24" height="28" fill="#1a0c06"/>
  </svg>
  <h3 class="service-name script" style="left:582px">Business</h3>
  <p class="service-text" style="left:628px">Built-to-order cabinet boxes and parts for cabinet shops and small contractors who install their own projects, cut and ready on schedule.</p>
</section>

<section class="gallery">
  <div class="shot" style="left:0;width:336px;background:
      radial-gradient(ellipse 120px 90px at 120px 250px,rgba(220,220,215,.35),rgba(0,0,0,0) 80%),
      linear-gradient(180deg,#5a5856 0%,#2a2826 30%,#1a1816 58%,#4a4440 72%,#8a8680 100%)"
      role="img" aria-label="Photo of a basement bar with dark cabinets and a stone-faced counter">
    <div class="shot-strip"></div>
    <h2 class="gallery-title script">Our Gallery</h2>
  </div>
  <div class="shot" style="left:344px;width:508px;background:
      radial-gradient(ellipse 160px 130px at 250px 470px,rgba(90,70,50,.7),rgba(0,0,0,0) 80%),
      linear-gradient(180deg,#ece8e0 0%,#e0dbd2 25%,#c4c2bc 50%,#8e8a84 70%,#4a3e34 100%)"
      role="img" aria-label="Photo of a white kitchen with stainless appliances and a granite island">
    <div class="shot-strip"></div>
  </div>
  <div class="shot" style="left:861px;width:339px;background:
      radial-gradient(ellipse 140px 110px at 180px 380px,rgba(240,236,228,.7),rgba(0,0,0,0) 80%),
      linear-gradient(180deg,#e4dfd6 0%,#cfc8bc 35%,#7a5a48 60%,#4e2e20 80%,#a08a74 100%)"
      role="img" aria-label="Photo of a white kitchen with a dark wood island">
    <div class="shot-strip"></div>
  </div>
  <div class="arrow" style="left:264px"><svg width="16" height="16" viewBox="0 0 16 16"><path d="M11 2 L5 8 L11 14" fill="none" stroke="#fff" stroke-width="2.5"/></svg></div>
  <div class="arrow" style="left:887px"><svg width="16" height="16" viewBox="0 0 16 16"><path d="M5 2 L11 8 L5 14" fill="none" stroke="#fff" stroke-width="2.5"/></svg></div>
</section>

<footer class="footer">
  <div class="brand"><span class="brand-dot"></span>BRINDLEWOOD</div>
  <p class="copyright">© 2015 Brindlewood Custom Cabinets. All rights reserved.</p>
  <div class="socials" aria-label="Social links"><span class="social"></span><span class="social"></span><span class="social"></span><span class="social"></span><span class="social"></span></div>
</footer>

</body>
</html>
```